Hearing Aid Company Website

Winner will be our future designer for our other brands. We need the website download to put into our Shopify account. We need a Shopify website done for a Hearing Aid Company called "Sonvel". We really need a creative modern site that has all the following pages that are also functional, not just empty pages. You can find stock photos and more online and information on hearing aids to add to the site. I will pay extra afterwards to really make the site exactly how I need after winner is picked. I've attached the necessary two products and also the pages I need on the site. I've also attached the logo. Make a really unique good looking site, feel free to add any pages or change anything you'd like you'd think would be best.
Top Page:
Hearing Aids (Products Attached)
Contact Us
Register your product (1 Year Warrenty)
Support
Track Order
Reviews
FAQ's
Careers
Bottom of Page:
Refund Policy
Privacy Policy
Terms of Conditions
Refund
Examples of websites I like:
https://quimbrelisten.com/
https://www.tovarlisteningaid.com/
https://www.plusaro.com/
https://www.vintu.com/
https://www.kolpe.com/
https://www.donmevo.com/

```html
<!DOCTYPE html>
<html lang="en">
<head>
<meta charset="utf-8">
<title>Sonvel — Hearing Aids</title>
<link href="https://fonts.googleapis.com/css2?family=Lato:wght@400;700;900&display=swap" rel="stylesheet">
<style>
:root{
  --blue:#0ba5ec;
  --ink:#1a1a1a;
  --muted:#4a4a4a;
  --panel:#e6e6e6;
  --tile:#ececec;
  --footer:#3b3b3b;
  --line:#e2e2e2;
}
*{box-sizing:border-box;margin:0;padding:0}
html,body{width:1200px;height:4125px;overflow:hidden;background:#fff}
body{position:relative;font-family:'Lato',sans-serif;color:var(--ink)}
.abs{position:absolute}
.btn{position:absolute;background:var(--blue);color:#fff;font-size:14px;display:flex;align-items:center;justify-content:center;border-radius:2px}
.blue{color:var(--blue);font-weight:700}
.photo{position:absolute;border-radius:4px;overflow:hidden}

/* header */
.logo{left:112px;top:30px;font-size:40px;font-weight:900;letter-spacing:-0.5px}
.nav a{position:absolute;top:44px;font-size:14px;color:var(--ink);text-decoration:none}
.nav .active{left:342px;top:37px;width:56px;height:33px;background:var(--blue);color:#fff;display:flex;align-items:center;justify-content:center;border-radius:2px}

/* hero */
.hero{left:34px;top:112px;width:1132px;height:599px;background:var(--panel);border-radius:16px;overflow:hidden}
.hero-photo{left:620px;top:0;width:512px;height:599px;border-radius:0;background:linear-gradient(180deg,#dcdcdc 0%,#cdb5a4 38%,#c09a84 62%,#8fbfe0 78%,#7fb4da 100%)}
.welcome{left:79px;top:118px;font-size:34px}
.brand{left:76px;top:176px;font-size:100px;font-weight:900;color:var(--blue);line-height:1}
.hero p{position:absolute;left:79px;top:300px;width:490px;font-size:21px;line-height:32px;color:var(--muted)}
.dots{left:531px;top:530px;display:flex;gap:7px}
.dots i{width:12px;height:12px;border-radius:50%;background:#9a9a9a}
.dots i:first-child{background:#111}

/* products */
.card{position:absolute;top:796px;width:481px;height:298px;background:var(--panel);border-radius:12px}
.card h3{position:absolute;left:35px;top:58px;font-size:33px;font-weight:900}
.card p{position:absolute;left:35px;top:110px;width:205px;font-size:15px;line-height:21px;color:var(--muted)}
.card .photo{right:40px;top:40px;width:190px;height:210px;border-radius:10px;background:linear-gradient(180deg,#e2e2e2 0%,#8c8c8c 55%,#3a3a3a 100%)}

/* section heads */
.head{left:0;width:1200px;text-align:center;font-size:42px}
.sub{left:0;width:1200px;text-align:center;font-size:16px;line-height:24px;color:var(--muted)}
.label{position:absolute;width:226px;text-align:center;font-size:23px;font-weight:700}

/* banner */
.banner{left:34px;top:1708px;width:1132px;height:523px;background:var(--panel);border-radius:16px;overflow:hidden}
.banner-photo{left:0;top:0;width:566px;height:523px;border-radius:0;background:linear-gradient(180deg,#d9d9d9 0%,#cfb09c 35%,#bd957e 60%,#6ea6d2 82%,#5b98c8 100%)}
.feature{position:absolute;left:662px;width:420px;display:flex;gap:24px;align-items:center;font-size:15px;line-height:22px;color:var(--muted)}
.feature svg{flex:none}

/* package */
.pack{position:absolute;top:2424px;width:226px;height:226px;border-radius:4px}

/* blog */
.post{position:absolute;top:2915px;width:309px}
.post .photo{position:relative;height:177px;border-radius:2px}
.post .date{margin-top:20px;font-size:13px;color:var(--muted);display:flex;gap:8px;align-items:center}
.post h4{margin-top:16px;font-size:20px;font-weight:400;line-height:28px}
.post .more{margin-top:12px;font-size:15px;font-weight:700;color:var(--blue)}
.arrow{position:absolute;top:2985px;width:40px;height:40px;background:var(--blue);border-radius:4px;display:flex;align-items:center;justify-content:center}

/* reviews */
.review{position:absolute;top:3394px;width:317px;height:226px;border:1px solid var(--line);border-radius:6px;padding:30px 24px;background:#fff}
.review.featured{background:var(--blue);border-color:var(--blue);color:#fff}
.stars{color:#f39a1c;font-size:16px;letter-spacing:1px}
.featured .stars{color:#fff}
.review p{margin-top:14px;font-size:14.5px;line-height:22px;color:var(--muted)}
.featured p{color:#fff}
.review .name{margin-top:18px;font-size:18px;color:var(--blue)}
.featured .name{color:#fff}
.review .when{margin-top:6px;font-size:13px;color:var(--muted)}
.featured .when{color:#fff}

/* footer */
.footer{left:0;top:3708px;width:1200px;height:417px;background:var(--footer);color:#fff}
.footer h5{position:absolute;top:76px;font-size:21px;font-weight:700}
.footer ul{position:absolute;top:134px;list-style:none;font-size:14.5px;line-height:38.5px}
.footer .about{position:absolute;left:112px;top:124px;width:320px;font-size:14.5px;line-height:26px}
.social{position:absolute;top:262px;display:flex;gap:18px;left:114px}
.social i{width:30px;height:30px;border-radius:50%;background:#fff}
.social i:first-child{background:var(--blue);border-radius:6px;width:36px;height:36px;margin-top:-3px}
.footer hr{position:absolute;left:112px;top:372px;width:976px;border:0;border-top:1px solid #5a5a5a}
.copy{position:absolute;left:0;top:387px;width:1200px;text-align:center;font-size:13px}
</style>
</head>
<body>

<header>
  <div class="abs logo">Sonvel</div>
  <nav class="nav">
    <a class="active">Home</a>
    <a style="left:432px">Hearing Aids</a>
    <a style="left:557px">Contact Us</a>
    <a style="left:669px">Support</a>
    <a style="left:764px">Track Order</a>
    <a style="left:880px">More ⌄</a>
  </nav>
  <svg class="abs" style="left:960px;top:40px" width="26" height="26" viewBox="0 0 24 24" fill="none" stroke="#222" stroke-width="2"><circle cx="10" cy="10" r="7"/><path d="M15 15l6 6"/></svg>
  <svg class="abs" style="left:1013px;top:40px" width="24" height="26" viewBox="0 0 24 24" fill="none" stroke="#222" stroke-width="2"><circle cx="12" cy="8" r="5"/><path d="M3 22c1-5 5-7 9-7s8 2 9 7z"/></svg>
  <svg class="abs" style="left:1063px;top:40px" width="26" height="24" viewBox="0 0 24 24" fill="none" stroke="#222" stroke-width="2"><path d="M1 3h4l3 12h12l3-9H7"/><circle cx="9" cy="20" r="1.5"/><circle cx="19" cy="20" r="1.5"/></svg>
</header>

<section class="abs hero">
  <div class="photo hero-photo" role="img" aria-label="Smiling man in a blue t-shirt wearing an in-ear hearing aid, shown in profile"></div>
  <div class="abs welcome">Welcome to</div>
  <div class="abs brand">Sonvel</div>
  <p>Excepteur sint occaecat cupidatat non proident, sunt in culpa qui officia deserunt mollit anim id est laborum."</p>
  <div class="btn" style="left:79px;top:431px;width:154px;height:43px">Shop Now</div>
  <div class="abs dots"><i></i><i></i><i></i><i></i></div>
</section>

<section>
  <div class="card" style="left:108px">
    <h3>Sonvel 1</h3>
    <p>Risus commodo viverra maecenas accumsan lacus vel facilisis.</p>
    <div class="btn" style="left:35px;top:195px;width:154px;height:43px">Shop Now</div>
    <div class="photo" role="img" aria-label="Sonvel 1 hearing aids in a round dark charging case"></div>
  </div>
  <div class="card" style="left:606px">
    <h3>Sonvel 2</h3>
    <p>Risus commodo viverra maecenas accumsan lacus vel facilisis.</p>
    <div class="btn" style="left:35px;top:195px;width:154px;height:43px">Shop Now</div>
    <div class="photo" role="img" aria-label="Sonvel 2 hearing aids above their open charging case"></div>
  </div>
</section>

<section>
  <div class="abs head" style="top:1170px">Four Modes,</div>
  <div class="abs head blue" style="top:1218px">Adapted to Avariety of Environments</div>
  <div class="abs sub" style="top:1284px">Hearing aid has four procedures, long press multifunctional keys 3s can adjust<br>hearing aid procedures. Suitable for a variety of environments</div>
  <div class="photo" style="left:111px;top:1364px;width:226px;height:226px;background:linear-gradient(180deg,#e9e4dc 0%,#c9a88a 55%,#8a7a52 100%)" role="img" aria-label="Family sharing a meal indoors"></div>
  <div class="photo" style="left:361px;top:1364px;width:226px;height:226px;background:linear-gradient(180deg,#d4d7d0 0%,#aea68a 50%,#7d6e4c 100%)" role="img" aria-label="Family walking outdoors in a field"></div>
  <div class="photo" style="left:612px;top:1364px;width:226px;height:226px;background:linear-gradient(180deg,#eeebe5 0%,#d1c6b5 55%,#9c9080 100%)" role="img" aria-label="Older adults talking around a table"></div>
  <div class="photo" style="left:863px;top:1364px;width:226px;height:226px;background:linear-gradient(180deg,#ddd2c6 0%,#c49a7e 50%,#6d8aa8 100%)" role="img" aria-label="Grandparents and children watching TV with popcorn"></div>
  <div class="label" style="left:111px;top:1598px">Indoor Mode</div>
  <div class="label" style="left:361px;top:1598px">Outdoor Mode</div>
  <div class="label" style="left:612px;top:1598px">Conference Mode</div>
  <div class="label" style="left:863px;top:1598px">TV Mode</div>
</section>

<section class="abs banner">
  <div class="photo banner-photo" role="img" aria-label="Smiling man touching the hearing aid in his ear"></div>
  <div class="abs" style="left:626px;top:88px;font-size:42px">Small and Comfortable</div>
  <div class="abs blue" style="left:626px;top:138px;font-size:42px">Easy to Operate</div>
  <div class="abs" style="left:628px;top:202px;width:420px;font-size:20px;line-height:28px;color:var(--muted)">Compact body, comfortable to wear; Easy to operate and adjust with other tools</div>
  <div class="feature" style="top:286px">
    <svg width="60" height="60" viewBox="0 0 60 60"><circle cx="30" cy="30" r="30" fill="#0ba5ec"/><path d="M26 42V24a3 3 0 016 0v9l7 2a3 3 0 012 4l-2 5H28z" fill="none" stroke="#fff" stroke-width="2"/><path d="M22 24a7 7 0 0114 0" fill="none" stroke="#fff" stroke-width="2"/></svg>
    <span>Quickly press the multifunctional key, hearing aid to changethe volume</span>
  </div>
  <div class="feature" style="top:370px">
    <svg width="60" height="60" viewBox="0 0 60 60"><circle cx="30" cy="30" r="30" fill="#0ba5ec"/><path d="M26 42V24a3 3 0 016 0v9l7 2a3 3 0 012 4l-2 5H28z" fill="none" stroke="#fff" stroke-width="2"/><circle cx="38" cy="18" r="5" fill="none" stroke="#fff" stroke-width="1.5"/></svg>
    <span>Long press the multifunctional key 3S, hearing aid switching program</span>
  </div>
</section>

<section>
  <div class="abs head" style="top:2306px">The Package <span class="blue">Includes</span></div>
  <div class="abs sub" style="top:2372px">Complete accessories, matching models, the best choice of similar products</div>
  <div class="pack" style="left:111px;background:linear-gradient(180deg,#ececec 0%,#6a6a6a 60%,#2c2c2c 100%)" role="img" aria-label="Round black charging case"></div>
  <div class="pack" style="left:361px;background:linear-gradient(180deg,#ececec 0%,#b9a98a 60%,#3a3a3a 100%)" role="img" aria-label="Pair of hearing aids"></div>
  <div class="pack" style="left:612px;background:linear-gradient(180deg,#d8d8d8 0%,#5a5a5a 55%,#1e1e1e 100%)" role="img" aria-label="Charging cable with USB plugs"></div>
  <div class="pack" style="left:863px;background:linear-gradient(180deg,#e0e0e0 0%,#7a7a7a 55%,#2a2a2a 100%)" role="img" aria-label="Small cleaning brush"></div>
  <div class="label" style="left:111px;top:2660px">Storage charging box</div>
  <div class="label" style="left:361px;top:2660px">Hearing aids</div>
  <div class="label" style="left:612px;top:2660px">Charge coil</div>
  <div class="label" style="left:863px;top:2660px">Cleaning brush</div>
  <div class="btn" style="left:523px;top:2717px;width:154px;height:42px">View All</div>
</section>

<section>
  <div class="abs head" style="top:2834px">Our <span class="blue">Blog</span></div>
  <div class="arrow" style="left:52px"><svg width="14" height="14" viewBox="0 0 14 14"><path d="M9 2L4 7l5 5" fill="none" stroke="#fff" stroke-width="2.4"/></svg></div>
  <div class="arrow" style="left:1106px"><svg width="14" height="14" viewBox="0 0 14 14"><path d="M5 2l5 5-5 5" fill="none" stroke="#fff" stroke-width="2.4"/></svg></div>
  <article class="post" style="left:111px">
    <div class="photo" style="background:linear-gradient(180deg,#ebebeb 0%,#b3b8c2 55%,#6c7180 100%)" role="img" aria-label="Older couple chatting at home"></div>
    <div class="date"><svg width="14" height="14" viewBox="0 0 14 14" fill="none" stroke="#0ba5ec"><rect x="1" y="2" width="12" height="11"/><path d="M1 5h12"/></svg>August 14 2024</div>
    <h4>Lorem ipsum dolor sit amet, consectetur adipiscing elit, sed do</h4>
    <div class="more">Read More</div>
  </article>
  <article class="post" style="left:444px">
    <div class="photo" style="background:linear-gradient(180deg,#e2ddd2 0%,#d9b45e 55%,#8f7e5c 100%)" role="img" aria-label="Young man studying at a desk"></div>
    <div class="date"><svg width="14" height="14" viewBox="0 0 14 14" fill="none" stroke="#0ba5ec"><rect x="1" y="2" width="12" height="11"/><path d="M1 5h12"/></svg>August 14 2024</div>
    <h4>Lorem ipsum dolor sit amet, consectetur adipiscing elit, sed do</h4>
    <div class="more">Read More</div>
  </article>
  <article class="post" style="left:776px">
    <div class="photo" style="background:linear-gradient(180deg,#f1e9e3 0%,#dcbca8 55%,#a8836f 100%)" role="img" aria-label="Audiologist fitting a hearing aid on a child"></div>
    <div class="date"><svg width="14" height="14" viewBox="0 0 14 14" fill="none" stroke="#0ba5ec"><rect x="1" y="2" width="12" height="11"/><path d="M1 5h12"/></svg>August 14 2024</div>
    <h4>Lorem ipsum dolor sit amet, consectetur adipiscing elit, sed do</h4>
    <div class="more">Read More</div>
  </article>
</section>

<section>
  <div class="abs head" style="top:3306px">What Our <span class="blue">Customers Say</span></div>
  <div class="review" style="left:111px">
    <div class="stars">★★★★★</div>
    <p>Excepteur sint occaecat cupidatat non proident, sunt in culpa qui officia deserunt mollit anim id est laborum.</p>
    <div class="name">Halloran</div><div class="when">August 14 2024</div>
  </div>
  <div class="review featured" style="left:441px">
    <div class="stars">★★★★★</div>
    <p>Excepteur sint occaecat cupidatat non proident, sunt in culpa qui officia deserunt mollit anim id est laborum.</p>
    <div class="name">Brenna</div><div class="when">August 14 2024</div>
  </div>
  <div class="review" style="left:771px">
    <div class="stars">★★★★★</div>
    <p>Excepteur sint occaecat cupidatat non proident, sunt in culpa qui officia deserunt mollit anim id est laborum.</p>
    <div class="name">Odalys</div><div class="when">August 14 2024</div>
  </div>
</section>

<footer class="abs footer">
  <h5 style="left:114px">About Us</h5>
  <p class="about">Excepteur sint occaecat cupidatat non proid, sunt in culpa qui quis nostrud exercitation ullamco laboris officia deserunt mollit anim id est laborum.</p>
  <div class="social"><i></i><i></i><i></i><i></i></div>
  <h5 style="left:516px">Quick Link</h5>
  <ul style="left:516px"><li>Home</li><li>Hearing Aids</li><li>Contact Us</li><li>Support</li><li>Track Order</li></ul>
  <h5 style="left:745px">Information</h5>
  <ul style="left:745px"><li>Reviews</li><li>FAQ's</li><li>Careers</li><li>Register</li><li>Blog</li></ul>
  <h5 style="left:947px">Other Links</h5>
  <ul style="left:947px"><li>Privacy Policy</li><li>Refund Policy</li><li>Terms of Service</li><li>Shipping Policy</li><li>Contact Information</li></ul>
  <hr>
  <div class="copy">Copyright © 2024 Sonvel. All rights reserved.</div>
</footer>

</body>
</html>
```